Waste and recycling company is looking for a design for our company guarantee

We are looking for a design for our company guarantee. This will then be added to our quote sheets and brochure and applied to our website. I am looking for quality and professionalism that speaks a million bucks.....It has to look like it is worth something!!! Be creative with the stars.
I am after 3 different sizes and some different colour versions. Sizes - The first 2 in a rectangle and the 3rd a square shape. The first one should be 200mm wide by 50 deep. The second 200 wide by 40 deep. The third 100 x 100.
Colour - Try first in black and white / Our Tandem waste blue / and then full colour using colours of our logo. No need to include our logo in the design.
Reason: 2 projects have to tie together.
Business customers.
Recycling

```html
<!DOCTYPE html>
<html lang="en">
<head>
<meta charset="utf-8">
<title>Five Star Customer Service Guarantee – Tandem waste</title>
<link rel="stylesheet" href="https://fonts.googleapis.com/css2?family=Cabin:wght@700&family=Alegreya+Sans:wght@400;700&family=Raleway:wght@400&display=swap">
<style>
  :root {
    --board: #444240;
    --paper: #ffffff;
    --star-red: #d0202e;
    --ink: #0d0d0d;
    --link-teal: #00858a;
    --label: #f2f2f2;
  }
  * { margin: 0; padding: 0; box-sizing: border-box; }
  html, body { width: 1200px; height: 900px; overflow: hidden; }
  body { background: var(--board); position: relative; font-family: "Alegreya Sans", sans-serif; }

  .size-label {
    position: absolute;
    font-family: "Raleway", sans-serif;
    font-size: 20px;
    color: var(--label);
    letter-spacing: 0.5px;
  }

  .guarantee {
    position: absolute;
    background: var(--paper);
    color: var(--ink);
  }
  .guarantee--wide  { left: 32px; top: 252px; width: 755px; height: 189px; }
  .guarantee--slim  { left: 32px; top: 462px; width: 755px; height: 151px; }
  .guarantee--square{ left: 809px; top: 252px; width: 362px; height: 362px; }

  .headline {
    position: absolute;
    font-family: "Cabin", sans-serif;
    font-weight: 700;
    text-align: right;
    text-transform: uppercase;
    white-space: nowrap;
    letter-spacing: 1.2px;
  }
  .headline span { display: block; }
  .headline .accent { color: var(--star-red); }

  .guarantee--wide .headline  { right: 481px; top: 18px; font-size: 43px; line-height: 37px; }
  .guarantee--slim .headline  { right: 509px; top: 10px; font-size: 36px; line-height: 31.5px; }
  .guarantee--square .headline{ right: 64px; top: 33px; font-size: 42px; line-height: 37.5px; }

  .star-column { position: absolute; fill: var(--star-red); }
  .guarantee--wide .star-column  { left: 289px; top: 20px; width: 30px; height: 154px; }
  .guarantee--slim .star-column  { left: 264px; top: 11px; width: 25px; height: 132px; }
  .guarantee--square .star-column{ left: 303px; top: 40px; width: 28px; height: 143px; }

  .promise { position: absolute; }
  .promise strong { font-weight: 700; }
  .terms { position: absolute; font-size: 12px; }
  .terms a { color: var(--link-teal); text-decoration: none; }

  .guarantee--wide .promise { left: 335px; top: 24px; font-size: 16.4px; line-height: 20px; }
  .guarantee--wide .terms   { left: 335px; top: 131px; line-height: 17px; }
  .guarantee--slim .promise { left: 306px; top: 19px; font-size: 15.6px; line-height: 18.6px; }
  .guarantee--slim .terms   { left: 306px; top: 101px; line-height: 15.5px; }
  .guarantee--square .promise { right: 31px; top: 193px; text-align: right; font-size: 14.3px; line-height: 17.8px; }
  .guarantee--square .terms   { right: 31px; top: 288px; text-align: right; font-size: 11px; line-height: 15.4px; }
</style>
</head>
<body>
<svg width="0" height="0" style="position:absolute" aria-hidden="true">
  <defs>
    <symbol id="star" viewBox="0 0 100 100">
      <polygon points="50,2 61.8,36.2 97.6,36.2 68.6,57.4 79.4,92.6 50,71 20.6,92.6 31.4,57.4 2.4,36.2 38.2,36.2"/>
    </symbol>
  </defs>
</svg>

<div class="size-label" style="left:32px; top:216px;">200mm x 50mm</div>
<div class="size-label" style="left:32px; top:626px;">200mm x 40mm</div>
<div class="size-label" style="left:809px; top:626px;">100mm x 100mm</div>

<section class="guarantee guarantee--wide">
  <h1 class="headline">
    <span class="accent">Five Star</span><span>Customer</span><span>Service</span><span class="accent">Guarantee</span>
  </h1>
  <svg class="star-column" viewBox="0 0 30 154" aria-hidden="true">
    <use href="#star" x="0" y="0" width="30" height="30"/>
    <use href="#star" x="0" y="31" width="30" height="30"/>
    <use href="#star" x="0" y="62" width="30" height="30"/>
    <use href="#star" x="0" y="93" width="30" height="30"/>
    <use href="#star" x="0" y="124" width="30" height="30"/>
  </svg>
  <p class="promise">You can have full confidence that Tandem will get the job done.<br>If we fail to do what is asked, in regards to scheduled<br>contracted services, on the allocated day given, then we will<br>do the job for <strong>FREE</strong> or refund you the cost of that service, up<br>to the value of $297.00.</p>
  <p class="terms">Please visit <a href="#">http://www.tandemwaste.com.au/service-terms.html</a><br>for full terms and conditions.</p>
</section>

<section class="guarantee guarantee--slim">
  <h2 class="headline">
    <span class="accent">Five Star</span><span>Customer</span><span>Service</span><span class="accent">Guarantee</span>
  </h2>
  <svg class="star-column" viewBox="0 0 25 132" aria-hidden="true">
    <use href="#star" x="0" y="0" width="25" height="25"/>
    <use href="#star" x="0" y="27" width="25" height="25"/>
    <use href="#star" x="0" y="53" width="25" height="25"/>
    <use href="#star" x="0" y="80" width="25" height="25"/>
    <use href="#star" x="0" y="107" width="25" height="25"/>
  </svg>
  <p class="promise">You can have full confidence that Tandem will get the job done.<br>If we fail to do what is asked, in regards to scheduled contracted<br>services, on the allocated day given, then we will do the job for <strong>FREE</strong><br>or refund you the cost of that service, up to the value of $297.00.</p>
  <p class="terms">Please visit <a href="#">http://www.tandemwaste.com.au/service-terms.html</a><br>for full terms and conditions.</p>
</section>

<section class="guarantee guarantee--square">
  <h2 class="headline">
    <span class="accent">Five Star</span><span>Customer</span><span>Service</span><span class="accent">Guarantee</span>
  </h2>
  <svg class="star-column" viewBox="0 0 28 143" aria-hidden="true">
    <use href="#star" x="0" y="0" width="28" height="28"/>
    <use href="#star" x="0" y="29" width="28" height="28"/>
    <use href="#star" x="0" y="58" width="28" height="28"/>
    <use href="#star" x="0" y="86" width="28" height="28"/>
    <use href="#star" x="0" y="115" width="28" height="28"/>
  </svg>
  <p class="promise">You can have full confidence that Tandem will get the<br>job done. If we fail to do what is asked, in regards to<br>scheduled contracted services, on the allocated day<br>given, then we will do the job for <strong>FREE</strong> or refund you<br>the cost of that service, up to the value of $297.00.</p>
  <p class="terms">Please visit<br><a href="#">http://www.tandemwaste.com.au/service-terms.html</a><br>for full terms and conditions.</p>
</section>
</body>
</html>
```